New business card design to go with our new logo

just want an eye-catching business card to go with our new logo. We are open to double sided or single sided. Just want it to have the following info on it. Whatever layout you think looks best.

First and Last Name
Title
Phone 801-555-7392
Address 214 W. Cedar Lane Pleasant Grove UT 84062
Email thecrew@marloweskennelandtreat.example

```html
<!DOCTYPE html>
<html lang="en">
<head>
<meta charset="utf-8">
<title>Marlowe's Kennel &amp; Treat – Business Card</title>
<link href="https://fonts.googleapis.com/css2?family=Open+Sans:wght@600;700&display=swap" rel="stylesheet">
<style>
  :root {
    --backdrop: #3b3b3d;
    --card-white: #ffffff;
    --brand-orange: #f68c4e;
    --brand-blue: #35a6dc;
    --ink-light: #ffffff;
  }
  * { margin: 0; padding: 0; box-sizing: border-box; }
  html, body {
    width: 1200px; height: 801px; overflow: hidden;
    background: var(--backdrop);
    font-family: "Open Sans", Arial, sans-serif;
  }
  .canvas { position: relative; width: 1200px; height: 801px; }
  .card {
    position: absolute; top: 273px;
    width: 446px; height: 255px;
    border-radius: 12px; overflow: hidden;
    background: var(--brand-orange);
  }
  .card--front { left: 135px; }
  .card--back { left: 622px; }
  .card__shape { position: absolute; inset: 0; width: 100%; height: 100%; }
  .card__shape path { fill: var(--card-white); }

  .brand {
    position: absolute;
    display: flex; align-items: center; gap: 8px;
    color: var(--brand-orange);
    font-weight: 700; line-height: 1.05;
  }
  .brand__dot { border-radius: 50%; background: var(--brand-blue); flex: none; }
  .brand__name { display: block; }
  .card--front .brand { left: 118px; top: 100px; font-size: 25px; }
  .card--front .brand__dot { width: 20px; height: 20px; }
  .card--back .brand { left: 18px; top: 102px; font-size: 15px; gap: 5px; }
  .card--back .brand__dot { width: 12px; height: 12px; }
  .brand__sub { display: block; font-size: 0.62em; }

  .holder {
    position: absolute; right: 24px; top: 25px;
    text-align: right; color: var(--ink-light);
    font-size: 12px; font-weight: 600; line-height: 17px;
  }
  .contact {
    position: absolute; left: 163px; top: 188px;
    list-style: none; color: var(--ink-light);
    font-size: 11.5px; font-weight: 600;
  }
  .contact__item { display: flex; align-items: center; gap: 6px; height: 16.5px; white-space: nowrap; }
  .contact__icon { width: 11px; height: 11px; flex: none; }
</style>
</head>
<body>
<main class="canvas">
  <section class="card card--front" aria-label="Business card front">
    <svg class="card__shape" viewBox="0 0 446 255" preserveAspectRatio="none" aria-hidden="true">
      <path d="M0 0 H285 C350 45 385 205 280 255 H0 Z"/>
    </svg>
    <div class="brand">
      <span class="brand__dot"></span>
      <span><span class="brand__name">MARLOWE'S</span><span class="brand__sub">Kennel &amp; Treat</span></span>
    </div>
  </section>

  <section class="card card--back" aria-label="Business card back">
    <svg class="card__shape" viewBox="0 0 446 255" preserveAspectRatio="none" aria-hidden="true">
      <path d="M0 0 H75 C180 60 180 200 80 255 H0 Z"/>
    </svg>
    <div class="brand">
      <span class="brand__dot"></span>
      <span><span class="brand__name">MARLOWE'S</span><span class="brand__sub">Kennel &amp; Treat</span></span>
    </div>
    <div class="holder">
      <p>First and Last Name</p>
      <p>Title</p>
    </div>
    <ul class="contact">
      <li class="contact__item">
        <svg class="contact__icon" viewBox="0 0 12 12" aria-hidden="true"><circle cx="6" cy="6" r="6" fill="#fff"/><path d="M3.6 3.2l1.2-.4.8 1.6-.7.6c.4.9 1 1.5 1.9 1.9l.6-.7 1.6.8-.4 1.2c-2.6-.2-4.8-2.4-5-5z" fill="#f68c4e"/></svg>
        Phone 801-555-7392
      </li>
      <li class="contact__item">
        <svg class="contact__icon" viewBox="0 0 12 12" aria-hidden="true"><circle cx="6" cy="6" r="6" fill="#fff"/><path d="M6 2.5a2.2 2.2 0 0 0-2.2 2.2C3.8 6.4 6 9.5 6 9.5s2.2-3.1 2.2-4.8A2.2 2.2 0 0 0 6 2.5zm0 3.1a.9.9 0 1 1 0-1.8.9.9 0 0 1 0 1.8z" fill="#f68c4e"/></svg>
        214 W. Cedar Lane Pleasant Grove UT 84062
      </li>
      <li class="contact__item">
        <svg class="contact__icon" viewBox="0 0 12 12" aria-hidden="true"><circle cx="6" cy="6" r="6" fill="#fff"/><circle cx="6" cy="6" r="3.3" fill="none" stroke="#f68c4e" stroke-width=".9"/><path d="M2.7 6h6.6M6 2.7c-1.6 2-1.6 4.6 0 6.6M6 2.7c1.6 2 1.6 4.6 0 6.6" fill="none" stroke="#f68c4e" stroke-width=".7"/></svg>
        thecrew@marloweskennelandtreat.example
      </li>
    </ul>
  </section>
</main>
</body>
</html>
```